"Use it or Lose it" and "Brush on Over"

We are a dental office looking to connect with our patients through direct mail advertising. With the last 3 months of the year coming we would like to send out Post Cards to our patients letting them know they have 3 months left to "USE IT OR LOSE IT" when it comes to their dental insurance benefits.
So we are looking for a post card that has the "Use It or Lost it" theme along with our dental office logo, telephone number and address.

We are also looking for a post card that says "Brush On Over" to remind our patients that they are due for a dental cleaning and we would like for them to come over to our dental office for a well needed cleaning :).

```html
<!DOCTYPE html>
<html lang="en">
<head>
<meta charset="utf-8">
<title>Linwood Dental – Use It or Lose It Postcard</title>
<link rel="stylesheet" href="https://fonts.googleapis.com/css2?family=Montserrat:wght@300;600;700&family=Raleway:wght@300&family=Lato:wght@400&display=swap">
<style>
  :root {
    --backdrop: #d0d1d3;
    --paper: #ffffff;
    --ink: #111111;
    --brand-blue: #1b63ad;
    --grad-blue: #4a98d6;
    --grad-mid: #8a6aa0;
    --grad-pink: #b1306a;
    --stamp: #c6c5c7;
    --rule: #8a8a8a;
    --text-dark: #333333;
  }
  * { margin: 0; padding: 0; box-sizing: border-box; }
  html, body { width: 1200px; height: 1200px; overflow: hidden; background: var(--backdrop); }
  .stage { position: relative; width: 1500px; height: 1500px; transform: scale(0.8); transform-origin: 0 0; }
  .card {
    position: absolute; left: 215px; width: 1070px; height: 680px;
    background: var(--paper); overflow: hidden;
    box-shadow: 4px 5px 8px rgba(0,0,0,0.25);
  }
  .card--front { top: 56px; }
  .card--back { top: 790px; }

  .side-tab {
    position: absolute; left: 0; top: 14px; width: 30px; height: 122px; border-radius: 15px;
    background: linear-gradient(90deg, var(--brand-blue), #3c8fd3);
  }

  .brand-name {
    position: absolute; display: flex; align-items: center; gap: 14px;
    font-family: "Montserrat", sans-serif; font-weight: 600;
    color: var(--brand-blue); letter-spacing: 1px; white-space: nowrap;
  }
  .brand-name .dot { border-radius: 50%; background: var(--brand-blue); flex: none; }
  .card--front .brand-name { right: 30px; top: 54px; font-size: 40px; }
  .card--front .brand-name .dot { width: 30px; height: 30px; }

  .headline-light {
    position: absolute; left: 25px; top: 212px; font-family: "Montserrat", sans-serif;
    font-weight: 300; font-size: 106px; line-height: 1; color: var(--ink);
  }
  .gradient-band {
    position: absolute; left: 0; top: 335px; width: 1070px; height: 145px;
    background: linear-gradient(90deg, var(--grad-blue), var(--grad-mid) 50%, var(--grad-pink));
  }
  .drip-decoration {
    position: absolute; left: 0; top: 480px; width: 1070px; height: 170px;
    background:
      linear-gradient(to bottom, rgba(255,255,255,0) 0%, rgba(255,255,255,0.55) 55%, #fff 100%),
      linear-gradient(90deg, var(--grad-blue), var(--grad-mid) 50%, var(--grad-pink));
  }
  .headline-bold {
    position: absolute; left: 27px; top: 358px; font-family: "Montserrat", sans-serif;
    font-weight: 700; font-size: 104px; line-height: 1; color: var(--paper);
  }
  .benefit-note {
    position: absolute; left: 638px; width: 400px; top: 401px; text-align: center;
    font-family: "Raleway", sans-serif; font-weight: 300; font-size: 19px; line-height: 23px;
    color: var(--paper);
  }

  .card--back .brand-name { left: 30px; top: 90px; font-size: 34px; gap: 20px; }
  .card--back .brand-name .dot { width: 60px; height: 60px; }
  .stamp { position: absolute; left: 865px; top: 20px; width: 130px; height: 148px; background: var(--stamp); }
  .address-to { position: absolute; left: 624px; top: 176px; font-family: "Lato", sans-serif; font-size: 18px; color: var(--text-dark); }
  .address-line { position: absolute; left: 621px; width: 367px; height: 1px; background: var(--rule); }

  .contact-band {
    position: absolute; left: 0; top: 264px; width: 555px; height: 145px;
    background: linear-gradient(90deg, var(--grad-blue), var(--grad-pink));
  }
  .contact-item {
    position: absolute; display: flex; align-items: center; gap: 27px;
    font-family: "Lato", sans-serif; font-size: 26px; white-space: nowrap;
  }
  .contact-item svg { width: 44px; height: 44px; flex: none; }
  .contact-band .contact-item { left: 27px; color: var(--paper); }
  .contact-band .contact-item:nth-child(1) { top: 18px; }
  .contact-band .contact-item:nth-child(2) { top: 84px; }
  .contact-row .contact-item { top: 454px; color: var(--text-dark); }

  .dot-decoration {
    position: absolute; left: 30px; top: 515px; width: 1020px; height: 150px;
    background: linear-gradient(90deg, var(--grad-blue), var(--grad-pink));
    opacity: 0.18;
  }
</style>
</head>
<body>
<div class="stage">

  <section class="card card--front">
    <div class="side-tab"></div>
    <div class="brand-name"><span class="dot"></span>LINWOOD DENTAL</div>
    <h1 class="headline-light">USE IT</h1>
    <div class="gradient-band"></div>
    <div class="drip-decoration" role="img" aria-label="Decorative dripping gradient pattern with scattered dots"></div>
    <h2 class="headline-bold">OR LOSE IT</h2>
    <p class="benefit-note">Use your dental insurance<br>benefit before 31st december or lose them</p>
  </section>

  <section class="card card--back">
    <svg width="0" height="0" style="position:absolute" aria-hidden="true">
      <defs>
        <linearGradient id="icon-grad" x1="0" y1="0" x2="1" y2="0">
          <stop offset="0" stop-color="#4a98d6"/>
          <stop offset="1" stop-color="#b1306a"/>
        </linearGradient>
      </defs>
    </svg>

    <div class="brand-name"><span class="dot"></span>LINWOOD DENTAL</div>

    <div class="stamp"></div>
    <span class="address-to">To</span>
    <div class="address-line" style="top:279px"></div>
    <div class="address-line" style="top:332px"></div>
    <div class="address-line" style="top:384px"></div>

    <div class="contact-band">
      <div class="contact-item">
        <svg viewBox="0 0 44 44" aria-hidden="true"><circle cx="22" cy="22" r="22" fill="#fff"/><path d="M22 11a7.5 7.5 0 0 0-7.5 7.5c0 5.5 7.5 14 7.5 14s7.5-8.5 7.5-14A7.5 7.5 0 0 0 22 11zm0 10.5a3 3 0 1 1 0-6 3 3 0 0 1 0 6z" fill="#4a7fc4"/></svg>
        <span>58 Maple Row Linwood, NJ 07016</span>
      </div>
      <div class="contact-item">
        <svg viewBox="0 0 44 44" aria-hidden="true"><circle cx="22" cy="22" r="22" fill="#fff"/><rect x="12" y="15" width="20" height="14" rx="2" fill="#4a7fc4"/><path d="M13 16l9 7 9-7" stroke="#fff" stroke-width="2" fill="none"/></svg>
        <span>linwooddental@mailbox.com</span>
      </div>
    </div>

    <div class="contact-row">
      <div class="contact-item" style="left:25px">
        <svg viewBox="0 0 44 44" aria-hidden="true"><circle cx="22" cy="22" r="22" fill="url(#icon-grad)"/><circle cx="22" cy="22" r="9" fill="none" stroke="#fff" stroke-width="2"/><path d="M13 22h18M22 13c-4 5-4 13 0 18M22 13c4 5 4 13 0 18" stroke="#fff" stroke-width="1.6" fill="none"/></svg>
        <span>linwooddental.com</span>
      </div>
      <div class="contact-item" style="left:405px">
        <svg viewBox="0 0 44 44" aria-hidden="true"><circle cx="22" cy="22" r="22" fill="url(#icon-grad)"/><rect x="13" y="19" width="18" height="11" rx="1.5" fill="#fff"/><rect x="17" y="13" width="10" height="7" fill="none" stroke="#fff" stroke-width="1.6"/></svg>
        <span>201 - 555 - 0148</span>
      </div>
      <div class="contact-item" style="left:721px;top:458px">
        <svg viewBox="0 0 44 44" aria-hidden="true"><circle cx="22" cy="22" r="22" fill="url(#icon-grad)"/><path d="M16 13l4 4-2.5 3c1.5 3 3.5 5 6.5 6.5l3-2.5 4 4-2.5 3c-7 0-15-8-15-15z" fill="#fff"/></svg>
        <span>201 - 555 - 0172</span>
      </div>
    </div>

    <div class="dot-decoration" role="img" aria-label="Decorative scattered gradient dots"></div>
  </section>

</div>
</body>
</html>
```